Make the invisible visible.... and attractive

I have an online course at http://www.brightpathlessons.example/Begin-today.html. I need an attractive graphic to sell the product. The course is a series of video, audio and handout materials set out in 32 lessons and has a free one year confidence course as a bonus.

Target Market(s)

Individuals who have problems with fear or anxiety.

Industry/Entity Type

Audio

```html
<!DOCTYPE html>
<html lang="en">
<head>
<meta charset="utf-8">
<title>Bright Path Lessons Online</title>
<link rel="stylesheet" href="https://fonts.googleapis.com/css2?family=Bebas+Neue&family=Roboto+Condensed:wght@700&family=Arimo:wght@400&display=swap">
<style>
  :root {
    --page: #ffffff;
    --band: #336699;
    --deep: #24558f;
    --mid: #4a7fc2;
    --light-sky: #7aa4dc;
    --accent-cyan: #33ccff;
    --accent-orange: #f7941d;
    --white: #ffffff;
    --seal: #2a64a0;
    --seal-edge: #1e4d7c;
    --button-top: #1a9cff;
    --button-bottom: #0a6fd6;
  }
  * { margin: 0; padding: 0; box-sizing: border-box; }
  html, body { width: 1200px; height: 1000px; overflow: hidden; background: var(--page); }
  .banner {
    position: absolute; left: 279px; top: 101px; width: 600px; height: 800px;
    background: linear-gradient(180deg, var(--deep) 12%, var(--mid) 55%, var(--light-sky) 62%, var(--band) 75%, var(--band) 100%);
    overflow: hidden; color: var(--white);
  }
  .header { position: absolute; left: 0; top: 0; width: 600px; height: 99px; background: var(--band); }
  .header-title {
    position: absolute; left: 29px; top: 30px; font-weight: 400;
    font-family: "Bebas Neue", sans-serif; font-size: 36px; line-height: 1; white-space: nowrap;
  }
  .brand-mark { position: absolute; left: 440px; top: 32px; display: flex; align-items: center; gap: 10px; }
  .brand-mark .dot { width: 32px; height: 32px; border-radius: 50%; border: 2px solid var(--white); }
  .brand-mark .name { font-family: "Arimo", sans-serif; font-size: 16px; color: var(--white); }
  .scene-photo {
    position: absolute; left: 0; top: 99px; width: 600px; height: 470px;
    background: linear-gradient(180deg, rgba(30,70,130,0.6) 0%, rgba(70,120,190,0.3) 70%, rgba(120,160,220,0.4) 100%);
  }
  .listener-photo {
    position: absolute; left: 0; top: 99px; width: 300px; height: 250px;
    background: radial-gradient(ellipse at 45% 45%, rgba(140,175,220,0.55) 0%, rgba(80,125,190,0.25) 55%, rgba(40,85,150,0) 80%);
  }
  .headline { position: absolute; left: 305px; top: 124px; width: 290px; font-family: "Roboto Condensed", sans-serif; font-weight: 700; }
  .headline .lead { font-size: 36px; line-height: 40px; }
  .headline .key { color: var(--accent-cyan); font-size: 66px; line-height: 62px; }
  .headline .tail { font-size: 34px; line-height: 40px; text-align: right; padding-right: 12px; margin-top: 2px; }
  .intro {
    position: absolute; left: 29px; top: 350px; width: 570px; white-space: nowrap;
    font-family: "Arimo", sans-serif; font-size: 19.5px; line-height: 27px;
  }
  .intro .cta-link { color: var(--accent-cyan); }
  .offer-get { position: absolute; left: 29px; top: 478px; font-family: "Roboto Condensed", sans-serif; font-weight: 700; font-size: 56px; line-height: 60px; }
  .offer-count { position: absolute; left: 205px; top: 480px; font-family: "Bebas Neue", sans-serif; font-size: 72px; line-height: 60px; color: var(--accent-orange); }
  .offer-unit { position: absolute; left: 78px; top: 535px; font-family: "Bebas Neue", sans-serif; font-size: 38px; line-height: 1; }
  .delivered { position: absolute; left: 76px; top: 578px; font-family: "Arimo", sans-serif; font-size: 19px; }
  .features {
    position: absolute; left: 42px; top: 615px; list-style: none;
    font-family: "Roboto Condensed", sans-serif; font-weight: 700; font-size: 25px; line-height: 27.5px; letter-spacing: 0.4px;
  }
  .features li { padding-left: 19px; text-indent: -19px; width: 250px; }
  .features li::before { content: "• "; }
  .bonus-seal { position: absolute; left: 290px; top: 472px; width: 244px; height: 244px; }
  .join-button {
    position: absolute; left: 395px; top: 738px; width: 186px; height: 42px;
    border: 1.5px solid var(--white); border-radius: 6px;
    background: linear-gradient(180deg, var(--button-top), var(--button-bottom));
    box-shadow: 4px 5px 6px rgba(0,0,0,0.45);
    font-family: "Arimo", sans-serif; font-size: 20px; color: var(--white);
    display: flex; align-items: center; justify-content: center; text-decoration: none;
  }
</style>
</head>
<body>
  <main class="banner">
    <div class="scene-photo" role="img" aria-label="Calm sky and sea backdrop in soft blue tones"></div>
    <div class="listener-photo" role="img" aria-label="Woman relaxing with eyes closed while wearing headphones"></div>

    <header class="header">
      <h1 class="header-title">Bright Path Lessons Online</h1>
      <div class="brand-mark"><span class="dot"></span><span class="name">Bright Path</span></div>
    </header>

    <h2 class="headline">
      <div class="lead">Develop powerful</div>
      <div class="key">emotional</div>
      <div class="key">resilience</div>
      <div class="tail">quickly and easily.</div>
    </h2>

    <p class="intro">Bright Path Lessons Online gives you everything you need<br>to be calm and composed in any situation. <span class="cta-link">Start right now.</span><br>By the end of today you will have everything you need to<br>return you to a calm and composed state, easily.</p>

    <div class="offer-get">Get the</div>
    <div class="offer-count">32</div>
    <div class="offer-unit">Lessons</div>
    <p class="delivered">delivered with</p>
    <ul class="features">
      <li>audio and video</li>
      <li>handouts material</li>
      <li>a workbook and</li>
      <li>exclusive forum for participants</li>
    </ul>

    <svg class="bonus-seal" viewBox="0 0 244 244" aria-label="Free bonus: one year long confidence course">
      <circle cx="122" cy="122" r="118" fill="var(--seal)" stroke="var(--seal-edge)" stroke-width="4"/>
      <g transform="translate(122 122) rotate(-20)" font-family="Bebas Neue, sans-serif" fill="#ffffff" text-anchor="middle">
        <text y="-22" font-size="52">FREE</text>
        <text y="14" font-size="36">BONUS</text>
        <text y="38" font-size="18">ONE YEAR LONG</text>
        <text y="56" font-size="18">CONFIDENCE COURSE</text>
        <text y="71" font-size="11">START RIGHT NOW</text>
      </g>
    </svg>

    <a class="join-button" href="http://www.brightpathlessons.example/Begin-today.html">Join Now</a>
  </main>
</body>
</html>
```